Hi! We require a design for business cards for directors and head teachers of an international daycare for children 0 - 9. We are family-owned, -operated and -oriented. We have six locations, looking to franchise. Our USPs are: 1) Flexibility 2) Quality teachers 3) International culture 4) Best nutrition We are quality teachers and professional caretakers, but with creativity and personality! Business cards should be playful (but no Comic Sans or baby hand prints), colorful (but no rainbows), and have some breathing space. It should be obvious from the business card that we're a daycare. In 2020 we'll be launching our new website based on this design: https://plomvane.io/47K2RQLWZTD The font in the new website will be Houschka (medium, demibold, bold). We will keep our current logo, included in the files here. There are also screenshots of some designs we like. Show us your best! :)

Industry/Entity Type

Childcare

Contact Information for Business Card

Lotte de Vries-Bakhuis
Communications Wizard
Poppel Hoek International Daycare
Kastanjeweg 47 B, 2316 KR Leiden
www.poppelhoek.nl
+31 647315082

Font styles to use
Serif
Sans Serif

Colors

Designer to choose colors to be used in the design.

Requirements
Must have
• Color

```html
<!DOCTYPE html>
<html lang="en">
<head>
<meta charset="utf-8">
<title>Poppel Hoek International Daycare – Business Cards</title>
<link href="https://fonts.googleapis.com/css2?family=Lato:wght@400;700;900&display=swap" rel="stylesheet">
<style>
  :root {
    --backdrop: #d6d6d6;
    --sunshine: #ffdd5c;
    --paper: #ffffff;
    --berry: #e84c81;
    --sky: #16a8de;
    --ink: #2a2a2a;
    --skin-warm: #c9976a;
    --skin-light: #f6dcc0;
  }
  * { margin: 0; padding: 0; box-sizing: border-box; }
  html, body { width: 1200px; height: 763px; overflow: hidden; }
  body {
    background: var(--backdrop);
    font-family: "Lato", sans-serif;
    position: relative;
  }
  .card {
    position: absolute;
    width: 433px;
    height: 257px;
    overflow: hidden;
  }
  .card--front { left: 115px; top: 224px; background: var(--sunshine); }
  .card--back  { left: 652px; top: 220px; background: var(--paper); }

  .swoosh { position: absolute; left: 0; top: 0; width: 433px; height: 257px; }

  .illustration { position: absolute; }
  .illustration--girl {
    left: 322px; top: -8px; width: 118px; height: 122px;
    border-radius: 0 0 0 60px;
    background: radial-gradient(circle at 45% 60%, var(--skin-warm) 0 55%, #5a3a24 56%);
  }
  .illustration--boy {
    left: -8px; top: 144px; width: 114px; height: 120px;
    border-radius: 0 60px 0 0;
    background: radial-gradient(circle at 40% 55%, var(--skin-light) 0 55%, #f2cf4a 56%);
  }

  .brand {
    position: absolute;
    text-align: center;
    color: var(--berry);
    font-weight: 900;
    font-size: 36px;
    line-height: 1;
    letter-spacing: 0.5px;
  }
  .card--front .brand { left: 117px; top: 96px; width: 200px; }
  .card--back .brand  { left: 0; top: 94px; width: 178px; font-size: 34px; }

  .tagline {
    position: absolute;
    color: var(--sky);
    font-size: 11.5px;
    text-align: center;
    letter-spacing: 0.2px;
  }
  .card--front .tagline { left: 117px; top: 181px; width: 200px; }
  .card--back .tagline  { left: 0; top: 184px; width: 178px; }

  .front-url {
    position: absolute;
    right: 10px; bottom: 9px;
    font-size: 10.5px;
    color: var(--ink);
  }

  .name-bar {
    position: absolute;
    left: 194px; top: 55px; width: 250px; height: 25px;
    background: var(--berry);
    border-radius: 7px 0 0 7px;
  }
  .name {
    position: absolute;
    left: 203px; top: 58px;
    font-size: 16.5px;
    color: var(--sky);
    text-transform: uppercase;
    white-space: nowrap;
  }
  .role {
    position: absolute;
    left: 202px; top: 85px;
    font-size: 10.5px;
    color: var(--sky);
    text-transform: uppercase;
  }

  .contact-line { position: absolute; left: 205px; top: 116px; width: 20px; height: 100px; }
  .contact {
    position: absolute;
    left: 229px;
    font-size: 12px;
    color: var(--berry);
    line-height: 1.05;
  }
  .contact--phone { top: 118px; }
  .contact--web   { top: 136px; }
  .contact--address { top: 182px; }
</style>
</head>
<body>

  <section class="card card--front">
    <svg class="swoosh" viewBox="0 0 433 257" aria-hidden="true">
      <path d="M80 240 C200 222 330 190 433 146 L433 176 C330 210 210 232 90 246 Z" fill="var(--berry)"/>
      <path d="M90 246 C210 232 330 210 433 176 L433 200 C330 228 210 246 95 252 Z" fill="var(--sky)"/>
    </svg>
    <div class="illustration illustration--girl" role="img" aria-label="Illustrated girl with a pink bow peeking in from the top right"></div>
    <div class="illustration illustration--boy" role="img" aria-label="Illustrated blond boy peeking in from the bottom left"></div>
    <div class="brand">Poppel<br>Hoek</div>
    <p class="tagline">INTERNATIONAL DAYCARE</p>
    <p class="front-url">www.poppelhoek.nl</p>
  </section>

  <section class="card card--back">
    <div class="brand">Poppel<br>Hoek</div>
    <p class="tagline">INTERNATIONAL DAYCARE</p>

    <div class="name-bar"></div>
    <h1 class="name">Lotte de Vries-Bakhuis</h1>
    <p class="role">Communications Wizard</p>

    <svg class="contact-line" viewBox="0 0 20 100" aria-hidden="true">
      <line x1="10" y1="10" x2="10" y2="72" stroke="var(--berry)" stroke-width="1.2"/>
      <path d="M4 2 l3 -1 2 4 -2 1.5 c1 2 2.5 3.5 4.5 4.5 l1.5 -2 4 2 -1 3 c-7 0 -12 -5 -12 -12z" fill="var(--sky)"/>
      <circle cx="10" cy="26" r="6" fill="var(--sky)"/>
      <path d="M4 26 h12 M10 20 v12 M6 22 q4 2 8 0 M6 30 q4 -2 8 0" stroke="#fff" stroke-width="0.8" fill="none"/>
      <path d="M10 84 c-3.5 -4 -5.5 -7 -5.5 -9.5 a5.5 5.5 0 0 1 11 0 c0 2.5 -2 5.5 -5.5 9.5z" fill="var(--sky)"/>
      <circle cx="10" cy="74.5" r="2" fill="#fff"/>
    </svg>
    <p class="contact contact--phone">+31 647315082</p>
    <p class="contact contact--web">www.poppelhoek.nl</p>
    <p class="contact contact--address">Poppel Hoek International Daycare<br>Kastanjeweg 47 B, 2316 KR Leiden</p>
  </section>

</body>
</html>
```